この度花灯経済新聞という業界紙の名刺広告のデザインを依頼させていただきます。
横向きの名刺サイズのデザインをお願いいたします。
分かりやすく、弊社らしいデザインにしていただけますと幸いでございます
ロゴは入れて頂けますと幸いでございます。

弊社URLを下記に記しますのでご参考ください。

https://www.corvalenhaus.co.jp/

何卒よろしくお願いいたします。
名刺サイズの広告ではありますが、名前や肩書が入っていないもので構いません。
何卒よろしくお願いいたします。

役員会議で決定されました。

皆様お忙しい中ご提案いただきましてありがとうございます。
また依頼する際は何卒よろしくお願いいたします。

```html
<!DOCTYPE html>
<html lang="ja">
<head>
<meta charset="utf-8">
<title>CORVALEN HAUS 名刺広告</title>
<link href="https://fonts.googleapis.com/css2?family=Noto+Serif+JP:wght@400;500&display=swap" rel="stylesheet">
<style>
  :root {
    --teal: #49bcc6;
    --gold: #a8923e;
    --ink: #555555;
    --paper: #ffffff;
    --bloom-light: #f3f4f1;
    --bloom-mid: #e4e8e2;
  }
  html, body {
    margin: 0;
    padding: 0;
    width: 870px;
    height: 1200px;
    overflow: hidden;
    background: var(--paper);
  }
  .sheet {
    position: relative;
    width: 870px;
    height: 1200px;
  }
  .card {
    position: absolute;
    font-family: "Noto Serif JP", serif;
  }
  .card--filled { left: 147px; top: 136px; width: 583px; height: 357px; }
  .card--outlined { left: 157px; top: 717px; width: 561px; height: 334px; }
  .card__frame {
    position: absolute;
    inset: 0;
    width: 100%;
    height: 100%;
  }
  .card__bloom {
    position: absolute;
    left: 7%;
    right: 7%;
    top: 38%;
    bottom: 8%;
    background: linear-gradient(180deg, rgba(243,244,241,0) 0%, var(--bloom-light) 35%, var(--bloom-mid) 100%);
    opacity: 0.85;
  }
  .card__brand {
    position: absolute;
    left: 0;
    right: 0;
    top: 41%;
    display: flex;
    justify-content: center;
    align-items: center;
    gap: 8px;
  }
  .brand__dot {
    width: 7px;
    height: 7px;
    border-radius: 50%;
    background: var(--gold);
  }
  .brand__name {
    color: var(--gold);
    font-size: 21px;
    font-weight: 500;
    letter-spacing: 0.02em;
    line-height: 1;
  }
  .card__tagline {
    position: absolute;
    top: 60%;
    margin: 0;
    color: var(--teal);
    font-size: 12px;
    font-weight: 500;
    line-height: 21px;
  }
  .card--filled .card__tagline { left: 8%; }
  .card--outlined .card__tagline { left: 5.8%; }
  .card__mission {
    position: absolute;
    top: 59.5%;
    margin: 0;
    color: var(--ink);
    font-size: 12px;
    line-height: 25px;
  }
  .card--filled .card__mission { left: 45%; }
  .card--outlined .card__mission { left: 44%; }
</style>
</head>
<body>
<main class="sheet">

  <section class="card card--filled">
    <svg class="card__frame" viewBox="0 0 583 357" preserveAspectRatio="none" aria-hidden="true">
      <rect x="0" y="0" width="583" height="357" fill="var(--teal)"/>
      <path d="M53 15 H530 A38 38 0 0 0 568 53 V304 A38 38 0 0 0 530 342 H53 A38 38 0 0 0 15 304 V53 A38 38 0 0 0 53 15 Z" fill="var(--paper)"/>
      <path d="M58 22 H525 A36 36 0 0 0 561 58 V299 A36 36 0 0 0 525 335 H58 A36 36 0 0 0 22 299 V58 A36 36 0 0 0 58 22 Z" fill="none" stroke="var(--teal)" stroke-width="1.5"/>
    </svg>
    <div class="card__bloom" role="img" aria-label="白い花とユーカリの葉を淡く重ねたフラワー写真"></div>
    <div class="card__brand">
      <span class="brand__dot"></span>
      <span class="brand__name">CORVALEN HAUS</span>
    </div>
    <p class="card__tagline">お客様には当日の感動を<br>企業様には感動の結果を<br>携わるスタッフには感動の人生を</p>
    <p class="card__mission">私たちCORVALEN HAUSは3つの感動を創造し、<br>限りある機会、時間を有効的に使い、<br>多くの企業様の結果に貢献する<br>ブライダルカンパニーです。</p>
  </section>

  <section class="card card--outlined">
    <svg class="card__frame" viewBox="0 0 561 334" preserveAspectRatio="none" aria-hidden="true">
      <path d="M40 5 H521 A35 35 0 0 0 556 40 V294 A35 35 0 0 0 521 329 H40 A35 35 0 0 0 5 294 V40 A35 35 0 0 0 40 5 Z" fill="var(--paper)" stroke="var(--teal)" stroke-width="7"/>
      <path d="M45 14 H516 A32 32 0 0 0 548 46 V288 A32 32 0 0 0 516 320 H45 A32 32 0 0 0 13 288 V46 A32 32 0 0 0 45 14 Z" fill="none" stroke="var(--teal)" stroke-width="1.5"/>
    </svg>
    <div class="card__bloom" role="img" aria-label="白い花とユーカリの葉を淡く重ねたフラワー写真"></div>
    <div class="card__brand">
      <span class="brand__dot"></span>
      <span class="brand__name">CORVALEN HAUS</span>
    </div>
    <p class="card__tagline">お客様には当日の感動を<br>企業様には感動の結果を<br>携わるスタッフには感動の人生を</p>
    <p class="card__mission">私たちCORVALEN HAUSは3つの感動を創造し、<br>限りある機会、時間を有効的に使い、<br>多くの企業様の結果に貢献する<br>ブライダルカンパニーです。</p>
  </section>

</main>
</body>
</html>
```